Vorlisk.com Redesign

Please read the notes and see the site-map attached.
Updates

We are looking for something highly creative. Please provide your best work. Best of luck and thank you very much for your hard work!

Project Deadline Extended
Reason: I am seeing good designs but I am not seeing great designs. I really need a design that is unique and is going to wow me. No one is required to stick to the existing color schemes etc. You are free to use other colors etc. I am seeing a lot of the same colors that are used on the site now.

Target Market(s)

Business and entrepreneurs mainly. People looking to build applications, software or launch web or mobile tech products.

Colors

Designer to choose colors to be used in the design.

Requirements
Must have
• See my attached html file.
Nice to have
Should not have
• No sure

```html
<!DOCTYPE html>
<html lang="en">
<head>
<meta charset="utf-8">
<title>Vorlisk.com</title>
<link rel="stylesheet" href="https://fonts.googleapis.com/css2?family=Play:wght@400;700&family=Arimo:wght@400;700&display=swap">
<style>
:root{
  --navy:#12263a;
  --footer:#0f2432;
  --footer-base:#0a1923;
  --green:#7cc242;
  --green-dark:#5e9f2c;
  --green-band:#78b944;
  --ink:#1c1c1c;
  --muted:#9a9a9a;
  --light:#f1f1f1;
  --line:#e2e2e2;
  --device:#e6e8ea;
  --blue:#2aa3d8;
  --white:#ffffff;
}
*{box-sizing:border-box;margin:0;padding:0}
html,body{width:1200px;height:2681px;overflow:hidden;background:var(--white)}
body{position:relative;font-family:"Arimo",Arial,sans-serif;color:var(--ink)}
h1,h2,h3,h4{font-weight:400}
.abs{position:absolute}

/* header + hero */
.hero{left:0;top:0;width:1200px;height:586px;background:linear-gradient(180deg,#1d3346 0%,#1a3a50 40%,#16364a 70%,#102b3c 100%)}
.hero-photo{left:0;top:141px;width:1200px;height:445px;background:radial-gradient(ellipse at 50% 40%,rgba(60,100,125,.5),rgba(16,40,56,.2) 70%)}
.brand{left:101px;top:30px;display:flex;align-items:center;gap:12px}
.brand-mark{width:40px;height:40px;border-radius:50%;background:var(--green)}
.brand-name{font-family:"Play",sans-serif;font-size:32px;color:var(--green)}
.topbar{top:12px;right:100px;display:flex;gap:40px;font-size:12px;color:#dfe6ea;align-items:center}
.topbar span{display:flex;align-items:center;gap:8px}
.nav{top:56px;right:100px;display:flex;gap:44px;align-items:center;font-family:"Play",sans-serif;font-size:16px;color:#f0f0f0}
.nav .active{color:var(--green)}
.client-login{background:var(--green);border:2px solid #b8e08f;border-radius:16px;padding:3px 20px;color:#fff;font-weight:700}
.service-bar{left:0;top:101px;width:1200px;height:40px;background:var(--green);display:flex;align-items:center;justify-content:center;gap:30px;font-family:"Play",sans-serif;font-size:15px;color:#fff}
.service-bar i{font-style:normal;opacity:.8}
.hero-title{left:0;top:245px;width:1200px;text-align:center;font-family:"Play",sans-serif;font-size:46px;color:#fff}
.hero-title b{font-size:58px;font-weight:700}
.hero-sub{left:0;top:312px;width:1200px;text-align:center;font-family:"Play",sans-serif;font-size:22px;color:#8c9ba6}
.hero-sub b{color:#d8dfe3;font-weight:400}
.read-more{left:501px;top:398px;width:167px;height:38px;border-radius:19px;background:var(--green);color:#fff;font-family:"Play",sans-serif;font-size:17px;text-align:center;line-height:38px}
.notch{left:586px;top:584px;width:0;height:0;border-left:14px solid transparent;border-right:14px solid transparent;border-top:16px solid #102b3c}

/* services */
.section-title{left:0;top:618px;width:1200px;text-align:center;font-family:"Play",sans-serif;font-size:42px;color:#111}
.device{background:var(--device)}
.service-title{font-family:"Play",sans-serif;font-size:22px;color:#333;letter-spacing:.5px}
.service-text{font-size:13px;line-height:24px;color:var(--muted);width:540px;letter-spacing:.55px}
.learn{font-size:13px;color:#222;letter-spacing:.4px}

/* testimonials */
.love{left:0;top:1628px;width:1200px;height:315px;background:linear-gradient(180deg,#86c54f,var(--green-band) 60%,#6fae3c)}
.love-title{left:0;top:1656px;width:1200px;text-align:center;font-family:"Play",sans-serif;font-size:24px;color:#fff;font-weight:700}
.avatar{border-radius:50%;border:4px solid #fff;background:#d8c7ba}
.bubble{border:2px solid rgba(255,255,255,.85);border-radius:8px;padding:10px 12px;font-size:11px;line-height:14px;color:#fff;width:279px;height:142px}
.person{font-size:11px;line-height:14px;color:#fff;text-align:center;width:200px}
.dot{width:9px;height:9px;border-radius:50%;background:#fff}

/* team */
.who-box{left:156px;top:1967px;width:886px;height:89px;background:var(--light)}
.who-rule{left:156px;top:2010px;width:886px;height:1px;background:var(--line)}
.who-icon{left:564px;top:1970px;width:72px;height:72px;border-radius:50%;background:#e2e2e2}
.who-title{left:0;top:2050px;width:1200px;text-align:center;font-family:"Play",sans-serif;font-size:22px;color:#444}
.member-photo{width:93px;height:93px;border-radius:50%;border:4px solid #dedede;background:#bdbdbd}
.member-name{width:200px;text-align:center;font-family:"Play",sans-serif;font-size:15px;line-height:17px;color:#333}
.shade{left:80px;top:2290px;width:1040px;height:18px;background:radial-gradient(ellipse at 50% 0%,rgba(0,0,0,.12),rgba(0,0,0,0) 70%)}

/* footer */
.footer{left:0;top:2430px;width:1200px;height:212px;background:var(--footer)}
.footer-notch{left:586px;top:2414px;border-left:14px solid transparent;border-right:14px solid transparent;border-bottom:16px solid var(--footer);width:0;height:0}
.foot-col{top:2466px;font-size:12px;line-height:20px;color:#8fa0ab}
.foot-col h4{font-family:"Play",sans-serif;font-size:12px;color:var(--blue);font-weight:700;margin-bottom:4px}
.contact{left:871px;top:2462px;font-size:12.5px;line-height:26.5px;color:#d7dde1;font-style:normal}
.base{left:0;top:2642px;width:1200px;height:39px;background:var(--footer-base);font-size:12px;color:#9aa7b0;line-height:39px;padding-left:103px}

/* chat */
.chat{left:869px;top:2305px;width:230px;height:126px;background:var(--green);border:2px solid var(--green-dark);border-radius:4px 4px 0 0}
.chat-head{font-family:"Play",sans-serif;font-size:12px;font-weight:700;color:#103010;text-align:center;margin-top:5px}
.chat-body{display:flex;align-items:center;gap:10px;padding:12px 12px 0 18px;font-family:"Play",sans-serif;font-size:24px;color:#fff}
.chat-dot{width:22px;height:22px;border-radius:50%;background:#fff;display:inline-block}
.chat-input{position:absolute;left:0;bottom:0;width:226px;height:32px;background:#eaf5df;font-size:12px;font-style:italic;color:#7a9a68;padding:8px 12px}
</style>
</head>
<body>

<header>
  <div class="abs hero"></div>
  <div class="abs hero-photo" role="img" aria-label="Blurred photo of a modern office workspace"></div>
  <div class="abs brand"><span class="brand-mark"></span><span class="brand-name">Vorlisk</span></div>
  <div class="abs topbar">
    <span><svg width="16" height="12" viewBox="0 0 16 12"><path d="M2 4c3-4 9-4 12 0l-2 2-2-1V3H6v2L4 6z" fill="#dfe6ea"/><rect x="4" y="7" width="8" height="4" rx="1" fill="#dfe6ea"/></svg>+1 (555) 014-2290</span>
    <span><svg width="16" height="12" viewBox="0 0 16 12"><rect x="1" y="1" width="14" height="10" fill="#dfe6ea"/><path d="M1 1l7 6 7-6" stroke="#12263a" fill="none"/></svg>reachus@vorlisk.com</span>
  </div>
  <nav class="abs nav">
    <span>Home</span><span>About Us</span><span>Our Work</span><span class="active">Services</span><span>Reach Us</span><span class="client-login">Client login</span>
  </nav>
  <div class="abs service-bar">
    <span>Web Development</span><i>/</i><span>Mobile App Development</span><i>/</i><span>Custom Software Development</span><i>/</i><span>User Experience Design</span>
  </div>
  <h1 class="abs hero-title">We create <b>Web</b> and <b>Mobile</b> products</h1>
  <p class="abs hero-sub">That delight users, create smiles and deliver more than <b>Expected</b></p>
  <div class="abs read-more">Read More</div>
  <div class="abs notch"></div>
</header>

<main>
  <h2 class="abs section-title">What We Do</h2>

  <div class="abs device" style="left:101px;top:707px;width:384px;height:263px" role="img" aria-label="Desktop computer product photo"></div>
  <h3 class="abs service-title" style="left:528px;top:710px">Web development</h3>
  <p class="abs service-text" style="left:528px;top:754px">Lorem ipsum dolor sit amet, consectetur adipiscing elit. Morbi non malesuada massa. Proin feugiat arcu nec vehicula vestibulum. In consequat at turpis sit amet placerat. Ut sit amet gravida lectus, in malesuada sem. Class aptent taciti sociosqu ad litora torquent per conubia nostra, per inceptos himenaeos. Praesent sodales nibh sit amet est venenatis pharetra. Phasellus vel nibh sed neque condimentum dictum vitae eget urna.</p>
  <span class="abs learn" style="left:528px;top:918px">Learn More &nbsp;&gt;&gt;</span>

  <h3 class="abs service-title" style="left:101px;top:1040px">Mobile App Development</h3>
  <p class="abs service-text" style="left:101px;top:1084px">Lorem ipsum dolor sit amet, consectetur adipiscing elit. Morbi non malesuada massa. Proin feugiat arcu nec vehicula vestibulum. In consequat at turpis sit amet placerat. Ut sit amet gravida lectus, in malesuada sem. Class aptent taciti sociosqu ad litora torquent per conubia nostra, per inceptos himenaeos. Praesent sodales nibh sit amet est venenatis pharetra. Phasellus vel nibh sed neque condimentum dictum vitae eget urna.</p>
  <span class="abs learn" style="left:101px;top:1248px">Learn More &nbsp;&gt;&gt;</span>
  <div class="abs device" style="left:667px;top:1020px;width:440px;height:253px" role="img" aria-label="Smartphone product photo"></div>

  <div class="abs device" style="left:101px;top:1343px;width:424px;height:233px" role="img" aria-label="Laptop product photo"></div>
  <h3 class="abs service-title" style="left:545px;top:1333px">Custom Software Development</h3>
  <p class="abs service-text" style="left:545px;top:1377px">Lorem ipsum dolor sit amet, consectetur adipiscing elit. Morbi non malesuada massa. Proin feugiat arcu nec vehicula vestibulum. In consequat at turpis sit amet placerat. Ut sit amet gravida lectus, in malesuada sem. Class aptent taciti sociosqu ad litora torquent per conubia nostra, per inceptos himenaeos. Praesent sodales nibh sit amet est venenatis pharetra. Phasellus vel nibh sed neque condimentum dictum vitae eget urna.</p>
  <span class="abs learn" style="left:545px;top:1541px">Learn More &nbsp;&gt;&gt;</span>

  <section>
    <div class="abs love" role="img" aria-label="Soft green blurred office background"></div>
    <h2 class="abs love-title">WHY CLIENTS LOVE US!</h2>

    <div class="abs avatar" style="left:123px;top:1736px;width:100px;height:100px" role="img" aria-label="Client portrait"></div>
    <div class="abs person" style="left:73px;top:1848px">Daniel Orbeck,<br>Partner-Halvern Stoke Inc</div>
    <p class="abs bubble" style="left:274px;top:1724px">From initial ideation, UX design, and layout to impeccable development and a flawless launch, Vorlisk was efficient, professional, and focused on positioning us for success. While I'd like to keep them as my secret go-to team of cyber ninjas, I feel obligated to "pay it forward".</p>

    <div class="abs avatar" style="left:634px;top:1736px;width:100px;height:100px" role="img" aria-label="Client portrait"></div>
    <div class="abs person" style="left:584px;top:1848px">Daniel Orbeck,<br>Partner-Halvern Stoke Inc</div>
    <p class="abs bubble" style="left:784px;top:1724px">From initial ideation, UX design, and layout to impeccable development and a flawless launch, Vorlisk was efficient, professional, and focused on positioning us for success. While I'd like to keep them as my secret go-to team of cyber ninjas, I feel obligated to "pay it forward".</p>

    <div class="abs dot" style="left:563px;top:1905px"></div>
    <div class="abs dot" style="left:578px;top:1905px"></div>
    <div class="abs dot" style="left:593px;top:1905px"></div>
  </section>

  <section>
    <div class="abs who-box"></div>
    <div class="abs who-rule"></div>
    <div class="abs who-icon"></div>
    <svg class="abs" style="left:582px;top:1990px" width="36" height="30" viewBox="0 0 36 30"><circle cx="18" cy="9" r="6" fill="#fff"/><path d="M7 28c0-8 5-12 11-12s11 4 11 12z" fill="#fff"/><circle cx="7" cy="12" r="4" fill="#fff"/><circle cx="29" cy="12" r="4" fill="#fff"/></svg>
    <h2 class="abs who-title">Who We Are</h2>

    <div class="abs member-photo" style="left:224px;top:2112px" role="img" aria-label="Team member portrait"></div>
    <div class="abs member-name" style="left:170px;top:2232px">John Doe,<br>Brightwell Studio</div>
    <div class="abs member-photo" style="left:446px;top:2112px" role="img" aria-label="Team member portrait"></div>
    <div class="abs member-name" style="left:392px;top:2232px">John Doe,<br>Brightwell Studio</div>
    <div class="abs member-photo" style="left:644px;top:2112px" role="img" aria-label="Team member portrait"></div>
    <div class="abs member-name" style="left:590px;top:2232px">John Doe,<br>Brightwell Studio</div>
    <div class="abs member-photo" style="left:854px;top:2112px" role="img" aria-label="Team member portrait"></div>
    <div class="abs member-name" style="left:800px;top:2232px">John Doe,<br>Brightwell Studio</div>
    <div class="abs shade"></div>
  </section>
</main>

<footer>
  <div class="abs footer"></div>
  <div class="abs footer-notch"></div>
  <div class="abs foot-col" style="left:107px"><h4>HOME</h4></div>
  <div class="abs foot-col" style="left:224px"><h4>ABOUT US</h4>Who We Are<br>Our Process</div>
  <div class="abs foot-col" style="left:360px"><h4>OUR WORK</h4></div>
  <div class="abs foot-col" style="left:504px"><h4>SERVICES</h4>Web Development<br>Mobile App Development<br>Custom Software Development<br>User Experience Design</div>
  <div class="abs foot-col" style="left:696px"><h4>REACH US</h4></div>
  <address class="abs contact">Vorlisk LLC<br>4820 Larkmont Ave #210<br>Brevard Falls, CA 90311<br>Voice: +1 (555) 014-2290<br>Email: reachus@vorlisk.com<br>Skype: vorlisk</address>
  <div class="abs base">© 2014 Vorlisk LLC. Privacy Policy</div>
</footer>

<aside class="abs chat">
  <div class="chat-head">Vorlisk Chat</div>
  <div class="chat-body"><span class="chat-dot"></span>we're online</div>
  <div class="chat-input">Type your message here</div>
  <svg class="abs" style="right:10px;bottom:10px" width="10" height="12" viewBox="0 0 10 12"><path d="M2 1l6 5-6 5" stroke="#5e9f2c" stroke-width="2" fill="none"/></svg>
</aside>

</body>
</html>
```